New York College Admissions Consulting Company Looking for a One-Page Flyer Design

We are a college admissions consulting company Brackwell Admissions Consulting (www.brackwelladmissions.example) and we help students apply to universities. We need a 1-page flyer design to hand out at a science competition for high school students. I attach all the information that should be included in the flyer and the logo. Please make a stylistic and professional looking flyer, which will impress these very smart and sophisticated high school students and even more importantly - their parents. Feel free to move the text around the flyer and to change the font as you see fit. Also, please add a stock picture or two, as you see fit. Also, let me know if I have to pay for the stock photos (if I have to get a license to use the photos on the flyer), and where and how much I would need to pay.

Target Market(s)

Smart and sophisticated high school students and even more importantly - their parents.

Industry/Entity Type

College

Requirements
Must have
• Must look sophisticated. This is an expensive service and parents need to know that our image matches our prices.
Should not have
• Wild colors like red.

```html
<!DOCTYPE html>
<html lang="en">
<head>
<meta charset="utf-8">
<title>Brackwell Admissions Consulting – Personal Statement Class</title>
<link rel="stylesheet" href="https://fonts.googleapis.com/css2?family=PT+Sans:wght@400;700&display=swap">
<style>
  :root {
    --ink: #1d2327;
    --navy: #1f3a56;
    --sky: #52c6ef;
    --sky-deep: #2f9fd6;
    --steel: #7f9cb3;
    --panel: #eef2f3;
    --paper: #ffffff;
    --rule: #2c3338;
  }
  * { margin: 0; padding: 0; box-sizing: border-box; }
  html, body { width: 927px; height: 1200px; overflow: hidden; background: var(--paper); }
  body { font-family: "PT Sans", Arial, sans-serif; color: var(--ink); }
  .flyer { position: relative; width: 927px; height: 1200px; background: var(--paper); overflow: hidden; }

  .brand { position: absolute; left: 62px; top: 78px; display: flex; align-items: center; gap: 16px; }
  .brand-dot { width: 40px; height: 40px; border-radius: 50%; background: var(--sky-deep); }
  .brand-name { font-weight: 700; font-size: 27px; color: var(--sky-deep); letter-spacing: 0.5px; }

  .contact { position: absolute; left: 603px; top: 78px; font-weight: 700; font-size: 16px;
    letter-spacing: 2.6px; color: var(--rule); line-height: 31px; }

  .panel { position: absolute; left: 77px; top: 260px; width: 791px; height: 883px; background: var(--panel); }

  .photo { position: absolute; left: 0; top: 193px; width: 533px; height: 304px;
    background: linear-gradient(180deg, #f4f8fa 0%, #dfe9ef 45%, #b9cbd6 62%, #e6eef2 100%); }

  .accent { position: absolute; left: 317px; top: 260px; width: 216px; height: 237px;
    background: linear-gradient(160deg, #5fcdf2 0%, #43b9e8 100%); }

  .quote { position: absolute; font-weight: 700; font-size: 70px; line-height: 1; color: var(--ink); }
  .quote-open { left: 327px; top: 268px; }
  .quote-close { left: 622px; top: 578px; }

  .title { position: absolute; left: 352px; top: 322px; width: 480px; font-weight: 700;
    font-size: 53px; line-height: 60px; color: var(--ink); letter-spacing: 0.5px; }

  .lede { position: absolute; left: 366px; top: 660px; width: 462px; text-align: right;
    font-weight: 700; font-size: 17.5px; line-height: 24px; color: var(--ink); }

  .band { position: absolute; left: 351px; top: 766px; width: 517px; height: 44px; background: var(--sky);
    color: var(--paper); font-weight: 700; font-size: 19px; letter-spacing: 2.4px;
    line-height: 44px; padding-left: 24px; }

  .card { position: absolute; left: 351px; width: 483px; background: var(--paper); }
  .date { top: 830px; height: 51px; font-weight: 700; font-size: 22.5px; line-height: 51px;
    padding-left: 22px; letter-spacing: 0.3px; }
  .agenda { top: 896px; height: 204px; padding: 22px 0 0 38px; }
  .agenda h2 { font-weight: 700; font-size: 26px; color: var(--sky); letter-spacing: 0.3px; }
  .agenda h2 .plain { color: var(--navy); }
  .agenda ul { list-style: none; margin-top: 16px; }
  .agenda li { font-weight: 700; font-size: 19.5px; line-height: 32px; color: var(--ink); }
  .agenda li .mark { margin-right: 8px; }
  .agenda li .hl { color: var(--sky); }

  .chart { position: absolute; left: 120px; top: 520px; }

  .stat-note { position: absolute; left: 116px; width: 200px; text-align: center;
    font-weight: 700; font-size: 11.5px; line-height: 15px; letter-spacing: 0.4px; text-transform: uppercase; }
  .stat-note.decline { top: 750px; }
  .stat-figure { position: absolute; left: 116px; top: 872px; width: 200px; text-align: center;
    font-family: "PT Serif", Georgia, serif; font-size: 38px; color: var(--ink); }
  .stat-rule { position: absolute; left: 147px; top: 926px; width: 139px; height: 5px; background: var(--rule); }
  .stat-note.essays { top: 945px; }
  .stat-note .small { font-size: 9.5px; }
</style>
</head>
<body>
<main class="flyer">
  <header>
    <div class="brand">
      <span class="brand-dot"></span>
      <span class="brand-name">BRACKWELL ADMISSIONS CONSULTING</span>
    </div>
    <div class="contact">
      <div>brackwelladmissions.example</div>
      <div>1.646.555.0142</div>
    </div>
  </header>

  <div class="panel"></div>
  <div class="photo" role="img" aria-label="Blurred crowd of students walking through a bright modern hall"></div>
  <div class="accent"></div>

  <span class="quote quote-open">“</span>
  <h1 class="title">The College Personal Statement and Perfecting Your Narrative</h1>
  <span class="quote quote-close">”</span>

  <p class="lede">Crafting the Perfect Narrative is vital to your college application. It can mean the difference between an acceptance and a rejection.</p>

  <div class="band">COMPLIMENTARY LIVE ONLINE CLASS</div>
  <div class="card date">SUNDAY, MAY 31, 2015 @ 4-5PM EST</div>

  <section class="card agenda">
    <h2>HOW-TO <span class="plain">and</span> LIVE Q&amp;A</h2>
    <ul>
      <li><span class="mark">&gt;&gt;</span> Avoid the <span class="hl">Most Common Mistakes</span></li>
      <li><span class="mark">&gt;&gt;</span> Compose a <span class="hl">Memorable Essay</span></li>
      <li><span class="mark">&gt;&gt;</span> Craft a <span class="hl">Compelling Narrative</span></li>
    </ul>
  </section>

  <svg class="chart" width="200" height="215" viewBox="0 0 200 215" aria-label="Admission rate 17.1% in 2005 and 8.8% in 2014">
    <text x="18" y="42" font-family="PT Serif, Georgia, serif" font-size="27" fill="var(--steel)">17.1%</text>
    <text x="87" y="104" font-family="PT Serif, Georgia, serif" font-size="27" fill="var(--sky)">8.8%</text>
    <rect x="27" y="55" width="34" height="128" fill="var(--steel)"/>
    <rect x="93" y="117" width="34" height="66" fill="var(--sky)"/>
    <rect x="19" y="183" width="156" height="2" fill="var(--rule)"/>
    <text x="44" y="204" text-anchor="middle" font-family="PT Sans, Arial, sans-serif" font-weight="700" font-size="10" fill="var(--steel)">2005</text>
    <text x="110" y="204" text-anchor="middle" font-family="PT Sans, Arial, sans-serif" font-weight="700" font-size="10" fill="var(--steel)">2014</text>
  </svg>

  <p class="stat-note decline">In the last<br>9 years, the average<br>Ivy League college<br>admission rate has<br>dropped by 49%.</p>

  <div class="stat-figure">25%</div>
  <div class="stat-rule"></div>
  <p class="stat-note essays">The personal<br>statement and the<br>supplemental essays<br><span class="small">comprise<br>approximately</span><br>25% of the<br>admission criteria.</p>
</main>
</body>
</html>
```